QV Wager needs banner to promote sign-ups

We need to put a banner on the homepage of our betting app / site to promote users who visit the site to sign-up for the platform. We are the largest blockchain based sports betting exchange. Our main markets are (in order) PCL, GRU, WQH, & ZJT. Users can bet in QWKT, VOR, or QV (our coin). It would be cool to feature those three coins if possible.
Our three main points we want to get to the user:
"Best Odds"
"Be the Bookmaker"
"Own the House"
We have provided images of our site and of our logos to incorporate in the site. One of the images shows the homepage of the site, this banner being designed will replace the small banners currently there if a user is not signed in. Additionally, we have included our sign-up page which shows the different ways users can sign in to the site (we want to show these options on the banner if possible).
Brand Book Dropbox
https://www.filecrate.example/sh/kpq4vmtrz8walx2/ZZR3hNqLmTwJeKdPoVbYcQ5x?dl=0
Sports betting & Blockchain

```html
<!DOCTYPE html>
<html lang="en">
<head>
<meta charset="utf-8">
<title>QV Wager — Sign-up Banner</title>
<link rel="stylesheet" href="https://fonts.googleapis.com/css2?family=Inter:wght@700;800&display=swap">
<style>
  :root {
    --page-bg: #03416d;
    --card-bg: #010306;
    --text: #ffffff;
    --tick: #3b8fd6;
    --sign-in: #2466d8;
    --sign-up: #55d0a8;
    --coin-a: #2a72c9;
    --coin-b: #6e7fe0;
    --coin-c: #1f9fc4;
  }
  * { box-sizing: border-box; margin: 0; padding: 0; }
  html, body { width: 1200px; height: 712px; overflow: hidden; }
  body {
    background: var(--page-bg);
    font-family: "Inter", Arial, sans-serif;
    color: var(--text);
    position: relative;
  }
  .banner {
    position: absolute;
    left: 75px; top: 75px;
    width: 1050px; height: 563px;
    border-radius: 22px;
    background: var(--card-bg);
    overflow: hidden;
  }
  .hero-visual { position: absolute; left: 0; top: 0; width: 1050px; height: 563px; }
  .brand {
    position: absolute; left: 45px; top: 28px;
    display: flex; align-items: center; gap: 10px;
    font-weight: 800; font-size: 24px; letter-spacing: -0.01em;
  }
  .brand-mark { width: 30px; height: 30px; background: var(--coin-c); border-radius: 50%; }
  .benefits {
    position: absolute; right: 82px; top: 204px;
    list-style: none; text-align: right;
  }
  .benefits li {
    display: flex; align-items: center; justify-content: flex-end;
    gap: 14px; height: 37.5px;
    font-weight: 700; font-size: 13px;
  }
  .benefits svg { width: 12px; height: 12px; }
  .actions {
    position: absolute; left: 750px; top: 331px;
    display: flex; gap: 8px;
  }
  .btn {
    width: 104px; height: 37px; border-radius: 19px;
    display: flex; align-items: center; justify-content: center;
    font-weight: 700; font-size: 13px; color: var(--text);
  }
  .btn-sign-in { background: var(--sign-in); }
  .btn-sign-up { background: var(--sign-up); }
  .coins {
    position: absolute; left: 724px; top: 404px;
    display: flex; gap: 18px; align-items: center;
  }
  .coin {
    width: 66px; height: 66px; border-radius: 50%;
    display: flex; align-items: center; justify-content: center;
    font-weight: 800; font-size: 13px; color: var(--text);
  }
  .coin-qwkt { background: var(--coin-a); }
  .coin-vor { background: var(--coin-b); }
  .coin-qv { background: var(--coin-c); }
</style>
</head>
<body>
  <section class="banner">
    <svg class="hero-visual" viewBox="0 0 1050 563" role="img" aria-label="Glowing teal and blue casino chips stacked in the dark, one large chip in front">
      <defs>
        <radialGradient id="chip-main" cx="0.7" cy="0.75" r="0.85">
          <stop offset="0" stop-color="#1c8a6e"/>
          <stop offset="0.55" stop-color="#0d4a5a"/>
          <stop offset="1" stop-color="#0a2c5e"/>
        </radialGradient>
        <radialGradient id="chip-back" cx="0.5" cy="0.5" r="0.6">
          <stop offset="0" stop-color="#0f5548"/>
          <stop offset="1" stop-color="#041914"/>
        </radialGradient>
        <radialGradient id="chip-far" cx="0.5" cy="0.5" r="0.6">
          <stop offset="0" stop-color="#1b3f8a"/>
          <stop offset="1" stop-color="#06122a"/>
        </radialGradient>
      </defs>
      <ellipse cx="495" cy="40" rx="190" ry="110" fill="url(#chip-back)" opacity="0.8"/>
      <ellipse cx="580" cy="210" rx="150" ry="95" fill="url(#chip-back)" opacity="0.5"/>
      <ellipse cx="945" cy="95" rx="180" ry="95" fill="url(#chip-far)" opacity="0.75"/>
      <circle cx="281" cy="285" r="235" fill="url(#chip-main)"/>
    </svg>
    <div class="brand"><span class="brand-mark"></span>QV Wager</div>
    <ul class="benefits">
      <li>BEST ODDS <svg viewBox="0 0 12 12"><circle cx="6" cy="6" r="6" fill="var(--tick)"/><path d="M3.3 6.2 5.2 8 8.8 4.2" stroke="#fff" stroke-width="1.5" fill="none"/></svg></li>
      <li>BE THE BOOKMAKER <svg viewBox="0 0 12 12"><circle cx="6" cy="6" r="6" fill="var(--tick)"/><path d="M3.3 6.2 5.2 8 8.8 4.2" stroke="#fff" stroke-width="1.5" fill="none"/></svg></li>
      <li>OWN THE HOUSE <svg viewBox="0 0 12 12"><circle cx="6" cy="6" r="6" fill="var(--tick)"/><path d="M3.3 6.2 5.2 8 8.8 4.2" stroke="#fff" stroke-width="1.5" fill="none"/></svg></li>
    </ul>
    <div class="actions">
      <a class="btn btn-sign-in">SIGN IN</a>
      <a class="btn btn-sign-up">SIGN UP</a>
    </div>
    <div class="coins">
      <div class="coin coin-qwkt">QWKT</div>
      <div class="coin coin-vor">VOR</div>
      <div class="coin coin-qv">QV</div>
    </div>
  </section>
</body>
</html>
```